Innovative Healthcare Technology Company needs a Business Card Design

We are in need of an innovative business card design for a new healthcare software company called "Lumenwise Data Partners". We develop software that creates medical assessment applications and mobile e-learning prevention services to reduce risk behaviors in adolescent and young adults. Our initial product, the "KESTREL App", conducts a tailored sexual risk assessment and provides a doctor with an insightful patient report to improve sexual risk counseling and ultimately reduce unintended pregnancy, STDs, etc.

We would like the design to incorporate our logo and branding colors (attached) in an innovative and creative manner. The final design should communicate professionalism and healthcare innovation. Our tag line is "prevention is the solution" (doesn't necessarily need to be included) and our target audience is doctors, medical directors, and medical business administrators. Please visit our website for additional info ourbrightmarq.com. Be creative and we look forward to seeing your designs!

Target Market(s)

healthcare - doctors, medical directors and medical business administrators

Industry/Entity Type

Healthcare

Contact Information for Business Card

We would like the design to incorporate our logo and branding colors (attached) in an innovative and creative manner. The final design should communicate professionalism and healthcare innovation. Our tag line is "prevention is the solution" (doesn't necessarily need to be included)

Font styles to use
Other font styles liked:
• quicksand

Requirements
Must have
• our logo and brand colors
• Name, (Mara Feldhovenik, PhD)
• Email (drmara@ourbrightmarq.com)
• phone (555.283.9170)
• Website (ourbrightmarq.com)
Should not have
• cartoon look

```html
<!DOCTYPE html>
<html lang="en">
<head>
<meta charset="utf-8">
<title>Lumenwise Data Partners — Business Card</title>
<link rel="stylesheet" href="https://fonts.googleapis.com/css2?family=Quicksand:wght@400;500;700&display=swap">
<style>
  :root {
    --brand-blue: #245e95;
    --brand-green: #79a990;
    --brand-grey: #9a9a9a;
    --ink: #2b2b2b;
    --paper: #ffffff;
    --stage: #ece9e4;
  }
  * { box-sizing: border-box; margin: 0; padding: 0; }
  html, body { width: 1200px; height: 1023px; overflow: hidden; }
  body {
    background: var(--stage);
    font-family: "Quicksand", sans-serif;
    position: relative;
  }
  .card {
    position: absolute;
    width: 580px;
    height: 331px;
    border-radius: 22px;
    overflow: hidden;
    box-shadow: 0 6px 18px rgba(0,0,0,0.14);
  }

  /* Front */
  .card-front { left: 60px; top: 130px; background: var(--paper); }
  .front-wordmark {
    position: absolute; left: 40px; top: 40px;
    display: flex; align-items: center; gap: 12px;
  }
  .wordmark-square { width: 22px; height: 22px; background: var(--brand-blue); }
  .wordmark-name {
    color: var(--brand-blue); font-weight: 500; font-size: 25px; line-height: 1.05;
  }
  .contact {
    position: absolute; right: 34px; top: 40px; text-align: right; color: var(--ink);
  }
  .contact-name { color: var(--brand-blue); font-weight: 700; font-size: 19px; letter-spacing: 0.3px; }
  .contact-title { font-size: 14px; margin-top: 4px; }
  .contact-lines { margin-top: 26px; list-style: none; font-size: 14px; }
  .contact-lines li { display: flex; justify-content: flex-end; align-items: center; gap: 8px; height: 21px; }
  .contact-lines svg { width: 14px; height: 14px; flex: none; }
  .address {
    position: absolute; left: 40px; bottom: 48px;
    font-size: 14px; line-height: 1.45; color: var(--ink);
  }
  .front-bands { position: absolute; left: 0; bottom: 0; width: 580px; height: 40px; }

  /* Back */
  .card-back {
    left: 560px; top: 560px; background: var(--brand-green);
    display: flex; align-items: center; justify-content: center;
  }
  .back-wordmark { display: flex; align-items: center; gap: 18px; }
  .back-wordmark .wordmark-square { width: 34px; height: 34px; }
  .back-wordmark .wordmark-name { font-size: 40px; }
</style>
</head>
<body>

<section class="card card-front" aria-label="Business card front">
  <div class="front-wordmark">
    <span class="wordmark-square"></span>
    <span class="wordmark-name">Lumenwise<br>Data Partners</span>
  </div>

  <div class="contact">
    <p class="contact-name">Mara Feldhovenik, PhD</p>
    <p class="contact-title">Managing Director</p>
    <ul class="contact-lines">
      <li>555.283.9170
        <svg viewBox="0 0 14 14" aria-hidden="true"><circle cx="7" cy="7" r="7" fill="var(--brand-blue)"/><path d="M4.3 3.6h1.6l.7 1.8-1 .7a5 5 0 0 0 2.3 2.3l.7-1 1.8.7v1.6c0 .5-.4.8-.9.8A6.3 6.3 0 0 1 3.5 4.5c0-.5.3-.9.8-.9z" fill="#fff"/></svg>
      </li>
      <li>drmara@ourbrightmarq.com
        <svg viewBox="0 0 14 14" aria-hidden="true"><circle cx="7" cy="7" r="7" fill="var(--brand-blue)"/><rect x="3.4" y="4.5" width="7.2" height="5" fill="none" stroke="#fff" stroke-width="1"/><path d="M3.4 4.5 7 7.3l3.6-2.8" fill="none" stroke="#fff" stroke-width="1"/></svg>
      </li>
      <li>www.ourbrightmarq.com
        <svg viewBox="0 0 14 14" aria-hidden="true"><circle cx="7" cy="7" r="7" fill="var(--brand-blue)"/><g fill="none" stroke="#fff" stroke-width="0.9"><circle cx="7" cy="7" r="4"/><ellipse cx="7" cy="7" rx="1.8" ry="4"/><path d="M3 7h8"/></g></svg>
      </li>
    </ul>
  </div>

  <p class="address">Your Home or Business<br>Address Put Here</p>

  <svg class="front-bands" viewBox="0 0 580 40" preserveAspectRatio="none" aria-hidden="true">
    <rect x="0" y="26" width="580" height="14" fill="var(--brand-blue)"/>
    <path d="M340 40 V22 Q340 4 360 4 H580 V40 Z" fill="var(--brand-green)"/>
  </svg>
</section>

<section class="card card-back" aria-label="Business card back">
  <div class="back-wordmark">
    <span class="wordmark-square"></span>
    <span class="wordmark-name">Lumenwise<br>Data Partners</span>
  </div>
</section>

</body>
</html>
```